Logo and Business Card Design for Innovative Corporate Law Firm

Valmor Advogados is a new, young and innovative law firm focused in corporate law, mainly helping start-ups in the incorporation process, liasing with strategic investors, funds, private equity and venture/seed capital businesses around the world.

We need a logo and business card design that correctly captures our modern and savvy, yet sober, approach to legal practice.

We are looking to starting with the logo and business card designs and further ahead move on to stationery, website etc.

We are located in São Paulo/Brazil, but we expect our logo and stationery design to be able to reach and connect to possible clients worldwide due to the international characteristic of our practice.

Be creative! We have no restrictions on colors, one-sided or two-sided cards, logos, font styles...
Updates

Guys, just to be clear: The project shall contemplate a full stationery design, but the logo and business card may be proposed in advance due to our urgent need to have these cards ready for our clients. The other stationery items may be proposed later on. Many thanks!

Dear all, please be aware that the logo should look good both in collor and black and white. 

Thanks

Industry/Entity Type

Business

Requirements
Must have
• Modern but sober approach
Nice to have
• I tend to like grey collor schemes with red touches, but this is not a must have...
Should not have
• Excessively bright, shiny look, that will make our legal services look too commercial. No excesses.

```html
<!DOCTYPE html>
<html lang="pt-BR">
<head>
<meta charset="utf-8">
<title>Valmor Advogados — Cartão de Visita</title>
<link rel="stylesheet" href="https://fonts.googleapis.com/css2?family=Oswald:wght@600&family=Century+Gothic&family=Questrial&display=swap">
<style>
  :root {
    --bg: #e6e6e8;
    --card-white: #fbfbfc;
    --card-shade: #eceef1;
    --brand-blue: #3447b0;
    --brand-blue-dark: #2a3a95;
    --ink: #3c3f45;
    --ink-soft: #55585e;
    --rule: #c9ccd3;
  }
  * { box-sizing: border-box; margin: 0; padding: 0; }
  html, body {
    width: 1200px; height: 1023px; overflow: hidden;
    background: var(--bg);
  }
  .canvas {
    width: 1200px; height: 1023px;
    display: flex; flex-direction: column; align-items: center; justify-content: center;
    gap: 56px;
  }
  .card {
    width: 760px; height: 434px; position: relative; overflow: hidden;
    box-shadow: 0 6px 18px rgba(0,0,0,.18);
  }

  /* Front */
  .card-front {
    background: linear-gradient(160deg, var(--card-white) 55%, var(--card-shade));
  }
  .card-front .band {
    position: absolute; left: 0; right: 0; bottom: 0; height: 40px;
    background: var(--brand-blue);
  }
  .wordmark {
    position: absolute; left: 62px; top: 150px;
    display: flex; align-items: center; gap: 16px;
  }
  .wordmark .dot {
    width: 50px; height: 50px; border-radius: 50%;
    background: var(--ink);
  }
  .wordmark .name {
    font-family: "Oswald", "Arial Narrow", sans-serif;
    font-weight: 600; font-size: 50px; letter-spacing: 1px;
    color: var(--ink); line-height: 1;
  }
  .person {
    position: absolute; left: 128px; top: 232px;
    font-family: "Questrial", "Century Gothic", sans-serif;
  }
  .person .person-name {
    color: var(--brand-blue); font-size: 19px; letter-spacing: .5px;
  }
  .person .person-role {
    color: var(--ink-soft); font-size: 15px; margin-top: 2px;
  }
  .contact {
    position: absolute; left: 300px; top: 282px;
    font-family: "Questrial", "Century Gothic", sans-serif;
    color: var(--ink); font-size: 15px; line-height: 1.4;
  }
  .contact .address { margin-bottom: 10px; }
  .contact .line { display: flex; align-items: center; gap: 8px; }
  .contact svg { width: 14px; height: 14px; flex: none; }

  /* Back */
  .card-back {
    background: linear-gradient(150deg, var(--brand-blue) 40%, var(--brand-blue-dark));
  }
  .card-back .back-mark {
    position: absolute; left: 0; right: 0; top: 168px; text-align: center;
    font-family: "Oswald", "Arial Narrow", sans-serif; font-weight: 600;
    font-size: 58px; letter-spacing: 1px; color: #ffffff; line-height: 1;
  }
  .card-back .back-web {
    position: absolute; left: 0; right: 0; top: 246px; text-align: center;
    font-family: "Questrial", "Century Gothic", sans-serif;
    font-size: 16px; letter-spacing: 1px; color: #ffffff;
  }
  .card-back .edge {
    position: absolute; left: 0; right: 0; bottom: 0; height: 8px;
    background: var(--card-white);
  }
</style>
</head>
<body>
<main class="canvas">
  <section class="card card-front" aria-label="Frente do cartão">
    <div class="wordmark">
      <span class="dot"></span>
      <span class="name">VALMOR ADVOGADOS</span>
    </div>
    <div class="person">
      <p class="person-name">RAFAEL COSTA</p>
      <p class="person-role">Position</p>
    </div>
    <div class="contact">
      <p class="address">Rua das Acácias 420, Torre 2, sala 305<br>São Paulo / SP - CEP: 04500-100</p>
      <p class="line">
        <svg viewBox="0 0 16 16" aria-hidden="true"><path d="M4 1.5l2.5 3-1.5 1.8a9 9 0 0 0 4.7 4.7L11.5 9.5l3 2.5-1.5 2.5C7 14.5 1.5 9 1.5 3z" fill="#3c3f45"/></svg>
        +55 11 4000-1234
      </p>
      <p class="line">
        <svg viewBox="0 0 16 16" aria-hidden="true"><rect x="1.5" y="3.5" width="13" height="9" fill="none" stroke="#3c3f45" stroke-width="1.4"/><path d="M1.5 3.5l6.5 5 6.5-5" fill="none" stroke="#3c3f45" stroke-width="1.4"/></svg>
        rcosta@valmoradvogados.com.br
      </p>
      <p class="line">
        <svg viewBox="0 0 16 16" aria-hidden="true"><circle cx="8" cy="8" r="6.5" fill="none" stroke="#3c3f45" stroke-width="1.3"/><ellipse cx="8" cy="8" rx="2.8" ry="6.5" fill="none" stroke="#3c3f45" stroke-width="1.1"/><path d="M1.5 8h13M2.6 4.8h10.8M2.6 11.2h10.8" stroke="#3c3f45" stroke-width="1"/></svg>
        www.valmoradvogados.com.br
      </p>
    </div>
    <div class="band"></div>
  </section>

  <section class="card card-back" aria-label="Verso do cartão">
    <p class="back-mark">VALMOR ADVOGADOS</p>
    <p class="back-web">www.valmoradvogados.com.br</p>
    <div class="edge"></div>
  </section>
</main>
</body>
</html>
```